Road Sign at our office 84 in X 48 in - Small Billboard

Kestrel Electrical
Electrical & Lighting Services

- we need a sign design for our small business/company based in Calhoun, GA called Kestrel Electrical - "our mission is to provide Northwest Georgia with dependable, high-quality electrical services that prioritize safety, integrity, and long-term reliability. As a woman-owned business with over 25 years of experience, we are committed to delivering exceptional workmanship and personalized service for every commercial, residential, and industrial project we undertake. We stand behind our work with a lifetime warranty—because your trust is our most powerful connection."

display logo, phone number, and open to other ideas without being cluttered, maybe instead of full website address, just use @ksrelectrical and it will send them to all of our website and socials...

it needs to be easy to read as they drive down the road
this is a place where people may be traveling at high speeds, make sure it's easy to see and understand at a glance.
It will be hanging 20-24ft from the ground. Like a small billboard.

https://ksrelectricworks.com/

Industry/Entity Type

Electrical Contractor

Requirements
Nice to have
• match the look and feel of website and socials

```html
<!DOCTYPE html>
<html lang="en">
<head>
<meta charset="utf-8">
<title>Kestrel Electrical – Road Sign</title>
<link rel="stylesheet" href="https://fonts.googleapis.com/css2?family=Montserrat:wght@600&family=Barlow+Semi+Condensed:wght@700&display=swap">
<style>
  :root {
    --sign-white: #ffffff;
    --spark-yellow: #f8b719;
    --volt-orange: #f05a2b;
    --ink: #231f20;
  }
  html, body {
    margin: 0;
    padding: 0;
    overflow: hidden;
    background: var(--sign-white);
  }
  .sign {
    position: relative;
    width: 1200px;
    height: 687px;
    overflow: hidden;
    background: var(--sign-white);
  }
  .sign__graphics {
    position: absolute;
    inset: 0;
    width: 1200px;
    height: 687px;
  }
  .fill-yellow { fill: var(--spark-yellow); }
  .fill-orange { fill: var(--volt-orange); }

  .brand {
    position: absolute;
    right: 37px;
    top: 96px;
    text-align: right;
    color: var(--ink);
    font-family: "Montserrat", sans-serif;
    font-weight: 600;
    line-height: 1;
  }
  .brand__name {
    display: block;
    font-size: 96px;
    letter-spacing: -1px;
  }
  .brand__trade {
    display: block;
    margin-top: 8px;
    margin-right: -0.55em;
    font-size: 34px;
    letter-spacing: 0.55em;
  }
  .brand__dot {
    position: absolute;
    left: 660px;
    top: 112px;
    width: 72px;
    height: 72px;
    border-radius: 50%;
    background: var(--volt-orange);
  }

  .contact {
    position: absolute;
    right: 37px;
    text-align: right;
    font-family: "Barlow Semi Condensed", sans-serif;
    font-weight: 700;
    line-height: 1;
    white-space: nowrap;
  }
  .contact--cta {
    top: 376px;
    font-size: 54px;
    color: var(--ink);
  }
  .contact--phone {
    top: 464px;
    font-size: 72px;
    letter-spacing: 1px;
    color: var(--sign-white);
  }
  .contact--handle {
    top: 578px;
    font-size: 72px;
    color: var(--ink);
  }
</style>
</head>
<body>
  <main class="sign">
    <svg class="sign__graphics" viewBox="0 0 1200 687" aria-hidden="true">
      <polygon class="fill-yellow" points="0,0 86,0 0,139"/>
      <polygon class="fill-yellow" points="88,0 88,264 352,264"/>
      <rect class="fill-yellow" x="0" y="423" width="88" height="264"/>
      <polygon class="fill-orange" points="352.5,264 481.5,264 226.5,669 1200,669 1200,687 87.75,687"/>
      <polygon class="fill-yellow" points="454.5,364.5 485,394.5 326,649 276,649"/>
      <polygon class="fill-yellow" points="480,448.5 511,448.5 385,649 355,649"/>
      <polygon class="fill-orange" points="746,448.5 1200,448.5 1200,551 681,551"/>
    </svg>

    <span class="brand__dot" aria-hidden="true"></span>
    <h1 class="brand" style="margin:0;">
      <span class="brand__name">Kestrel</span>
      <span class="brand__trade">ELECTRICAL</span>
    </h1>

    <p class="contact contact--cta" style="margin:0;">Call Now</p>
    <p class="contact contact--phone" style="margin:0;">706-555-0148</p>
    <p class="contact contact--handle" style="margin:0;">@ksrelectrical</p>
  </main>
</body>
</html>
```